Buchcover spirituelles Projekt 12 x 19 cm
Zielgruppe
Meine Zielgruppe sind Menschen die an Grundwissen über Spiritualität und die Kraft der Gedanken interessiert sind und den Glauben besitzen mit der Kraft Ihrer Gedanken Ihr Leben zu verändern.
Aufgabenstellung
Ich suche ein Cover in 12 x 19 cm für ein Grundlagenwerk über Affirmationen. Inhalt des Buches sind Anleitungen mit dem Umgang von Affirmationen in Bezug auf Energie-Zentren und Lebensthemen.
Titel:
LEUCHTPFAD DER BEJAHUNGEN
Gesundheit für Körper und Seele
von Hannelore Wachtl & Ferdinand Wohlgemuth
Auf der Vorderseite sollte noch ein Hinweis sein: inklusive Gratis-Download der Meditation "Die Quelle der Klärung, Stärkung und Erneuerung"
Auf der Rückseite soll ein kleiner Text sein und unser Foto (Siehe Anhang), Platz für den Strichcode
Aktuell interessiert uns nur das Design. Wenn der Satz fertig ist in ca vier Wochen, müsste dann genau nachgearbeitet werden. Dann können wir auch genaue Angaben machen wegen Buchrückendicke, ISBN -Nummer etc. mitteilen. Diese Arbeit sollte im Preis enthalten sein und nicht zusätzlich nachhonoriert werden.
Wir benötigen dann 3 verschiedene Versionen des Umschlags für:
HardCover
SoftCover
eBook
Wir haben keine Präferenzen bezüglich der Gestaltung, nur bitte nicht düster oder gruselig.
Nachsatz_
Wir möchten, unser Foto auch auf der Vorderseite zu sehen ist, sprich freigestellt und auf möglichst einfarbigen Hintergrund zu sehen ist. Hier sind wir aber offen.

```html
<!DOCTYPE html>
<html lang="de">
<head>
<meta charset="utf-8">
<title>Leuchtpfad der Bejahungen – Buchcover</title>
<link href="https://fonts.googleapis.com/css2?family=Cinzel:wght@400;700&family=Marcellus+SC&display=swap" rel="stylesheet">
<style>
  :root {
    --page-bg: #eceeef;
    --sky-light: #a8e6f6;
    --sky-mid: #5cc4ec;
    --sky-deep: #3a9fe0;
    --title-gold: #f5cf2a;
    --subtitle-blue: #4d8fd6;
    --badge-blue: #4fc1e9;
    --band-yellow: #f7cf2e;
    --white: #ffffff;
  }
  * { margin: 0; padding: 0; box-sizing: border-box; }
  html, body {
    width: 1200px; height: 800px; overflow: hidden;
    background: var(--page-bg);
  }
  .cover {
    position: absolute; left: 360px; top: 20px;
    width: 480px; height: 760px; overflow: hidden;
    background: radial-gradient(ellipse at 50% 40%, var(--sky-light) 0%, var(--sky-mid) 45%, var(--sky-deep) 100%);
    font-family: "Cinzel", serif;
  }
  .title {
    position: absolute; top: 48px; left: 0; width: 100%;
    text-align: center; color: var(--title-gold);
    font-weight: 700; font-size: 46px; line-height: 1.3; letter-spacing: 1px;
  }
  .subtitle {
    position: absolute; top: 258px; left: 0; width: 100%;
    text-align: center; color: var(--subtitle-blue);
    font-family: "Marcellus SC", serif; font-size: 27px; line-height: 1.3;
  }
  .portrait {
    position: absolute; left: 0; top: 340px; width: 480px; height: 350px; z-index: 1;
  }
  .author-band {
    position: absolute; left: 0; bottom: 0; width: 100%; height: 86px; z-index: 2;
    background: var(--band-yellow);
    text-align: center; color: var(--white);
    font-family: "Marcellus SC", serif;
  }
  .author-by { font-size: 20px; padding-top: 14px; }
  .author-names { font-size: 20px; margin-top: 4px; letter-spacing: 0.5px; }
  .badge {
    position: absolute; left: 16px; top: 520px; z-index: 3;
    width: 190px; height: 190px; border-radius: 50%;
    background: var(--badge-blue);
    display: flex; flex-direction: column; align-items: center; justify-content: center;
    text-align: center; padding: 0 16px;
  }
  .badge-label { color: var(--title-gold); font-weight: 700; font-size: 18px; margin-bottom: 6px; }
  .badge-text {
    color: var(--white); font-family: "Marcellus SC", serif;
    font-size: 13px; line-height: 1.25;
  }
</style>
</head>
<body>
  <div class="cover">
    <h1 class="title">LEUCHTPFAD<br>DER<br>BEJAHUNGEN</h1>
    <p class="subtitle">Gesundheit<br>für Körper und Seele</p>
    <svg class="portrait" role="img" aria-label="Freigestelltes Foto der beiden Autoren, eine Frau und ein Mann in weißen Hemden, lächelnd zum Himmel blickend" viewBox="0 0 480 350" preserveAspectRatio="none">
      <defs>
        <linearGradient id="portraitTone" x1="0" y1="0" x2="0" y2="1">
          <stop offset="0" stop-color="#ffffff" stop-opacity="0"/>
          <stop offset="0.35" stop-color="#f2e6d8" stop-opacity="0.55"/>
          <stop offset="1" stop-color="#f4f1ee" stop-opacity="0.9"/>
        </linearGradient>
      </defs>
      <path d="M40 350 L60 200 Q120 40 200 60 Q300 70 320 180 Q380 140 440 200 L470 350 Z" fill="url(#portraitTone)"/>
    </svg>
    <div class="author-band">
      <div class="author-by">von</div>
      <div class="author-names">Hannelore Wachtl &amp; Ferdinand Wohlgemuth</div>
    </div>
    <div class="badge">
      <div class="badge-label">INKLUSIVE</div>
      <div class="badge-text">Gratis-Download der Meditation „Die Quelle der Klärung, Stärkung und Erneuerung“</div>
    </div>
  </div>
</body>
</html>
```